looking for sleek business card to standout from the crowd!

We are a young biotechnology company looking to help you personalize your health through understanding your genetic make up. We need you help in making a clean but sleek business card design using our new logo. The goal? Any time we give our cards out, people say "nice card!" The feel we are going for is "modern-techy". We don't want to come across as an old, giant pharma company, but not trying to be a hipster either.

Target Market(s)

healthcare and biotechnology industry.

Industry/Entity Type

Biotechnology

Contact Information for Business Card

Info to include on the card will be NAME, TITLE, EMAIL, PHONE. The companies website (www.corvalinbio.com) should also be on the card some where. Would like the logo, when printed, to be raised.

Requirements
Must have
• The logo we have attached in the color it is in. Fonts for text should lean toward more professional/tech.
Nice to have
• Prefer white/light color background
Should not have
• cartoons, landscape backgrounds images.

```html
<!DOCTYPE html>
<html lang="en">
<head>
<meta charset="utf-8">
<title>Corvalin Business Card</title>
<link href="https://fonts.googleapis.com/css2?family=Didact+Gothic&display=swap" rel="stylesheet">
<style>
  :root {
    --backdrop: #e6e8eb;
    --card: #ffffff;
    --maroon: #87171a;
    --lime: #8cc63f;
    --ink: #1a1a1a;
    --paper: #ffffff;
  }
  * { margin: 0; padding: 0; box-sizing: border-box; }
  html, body {
    width: 1200px; height: 1200px; overflow: hidden;
    background: var(--backdrop);
    font-family: "Didact Gothic", "Helvetica Neue", Arial, sans-serif;
  }
  .canvas { position: relative; width: 1200px; height: 1200px; }
  .card {
    position: absolute; left: 204px; width: 808px; height: 492px;
    background: var(--card);
    box-shadow: 0 4px 14px rgba(0,0,0,0.12);
    overflow: hidden;
  }
  .card--front { top: 76px; }
  .card--back { top: 630px; }
  .card__art { position: absolute; inset: 0; }

  .company-name {
    position: absolute; display: flex; align-items: center;
    color: var(--paper); white-space: nowrap; letter-spacing: 0.04em;
  }
  .card--front .company-name {
    left: 0; right: 0; top: 116px; height: 262px; justify-content: center;
    font-size: 84px;
  }
  .card--back .company-name {
    left: 30px; top: 216px; height: 60px; font-size: 40px;
  }

  .holder {
    position: absolute; left: 414px; top: 122px;
    font-size: 46px; color: var(--ink); letter-spacing: 0.03em;
  }
  .contact-list { position: absolute; left: 416px; top: 212px; list-style: none; }
  .contact-list__item {
    display: flex; align-items: center; gap: 10px;
    height: 40px; margin-bottom: 19px;
    font-size: 28px; color: var(--ink); letter-spacing: 0.02em;
  }
  .contact-list__icon { width: 38px; height: 38px; flex: none; }
</style>
</head>
<body>
<main class="canvas">
  <section class="card card--front" aria-label="Card front">
    <svg class="card__art" viewBox="0 0 808 492" aria-hidden="true">
      <rect x="0" y="116" width="808" height="262" fill="var(--maroon)"/>
      <polygon points="0,116 96,116 0,212" fill="var(--lime)"/>
    </svg>
    <div class="company-name">CORVALIN</div>
  </section>

  <section class="card card--back" aria-label="Card back">
    <svg class="card__art" viewBox="0 0 808 492" aria-hidden="true">
      <polygon points="0,116 394,116 294,378 0,378" fill="var(--maroon)"/>
      <line x1="404" y1="116" x2="304" y2="378" stroke="var(--lime)" stroke-width="3"/>
    </svg>
    <div class="company-name">CORVALIN</div>

    <p class="holder">Nema Title</p>
    <ul class="contact-list">
      <li class="contact-list__item">
        <svg class="contact-list__icon" viewBox="0 0 38 38" aria-hidden="true">
          <circle cx="19" cy="19" r="18" fill="var(--lime)"/>
          <rect x="10" y="13" width="18" height="12" fill="#fff"/>
          <polyline points="10,13 19,20 28,13" fill="none" stroke="var(--lime)" stroke-width="1.6"/>
        </svg>
        <span>Email</span>
      </li>
      <li class="contact-list__item">
        <svg class="contact-list__icon" viewBox="0 0 38 38" aria-hidden="true">
          <circle cx="19" cy="19" r="18" fill="var(--lime)"/>
          <path d="M13 10 l4 0 l2 5 l-3 2 q2 4 6 6 l2 -3 l5 2 l0 4 q-1 2 -3 2 q-10 -1 -15 -13 q0 -3 2 -5z" fill="#fff"/>
        </svg>
        <span>Phone</span>
      </li>
      <li class="contact-list__item">
        <svg class="contact-list__icon" viewBox="0 0 38 38" aria-hidden="true">
          <circle cx="19" cy="19" r="18" fill="var(--lime)"/>
          <g fill="none" stroke="#fff" stroke-width="1.8">
            <circle cx="19" cy="19" r="9"/>
            <ellipse cx="19" cy="19" rx="4" ry="9"/>
            <line x1="10" y1="19" x2="28" y2="19"/>
          </g>
        </svg>
        <span>corvalinbio.com</span>
      </li>
    </ul>
  </section>
</main>
</body>
</html>
```